An expert for Professional and Technical Evaluation of Painting Work Needs a New Letterhead Design

I own a mid-sized painting company and also work as an expert for professional and technical evaluation of painting work in the area of Zurich.

Please read the project description and the must-have-requirements carefully!

I attached 1 PDF which will help you create a new letterhead design:

THE NEW DESIGN DOESN'T NEED A LOGO! (Because it won't represent a company, it represents only a service)
Updates

Dear designers We had a discussion about the location/placement of the design and came to the conclusion that we only want the design to be in the header area of the A4-paper. We would be glad to receive some revised version of your designs. Thank you and kind regards!

Project Deadline Extended
Reason: Due to the fact that only 20% of the designer have understood the brief and submitted designs that have met the requirements we decided to extend the contest deadline.

Project Deadline Extended
Reason: A great deal of good designs were submitted in the last few days. A big thank you to all the participating designers for your good work. We need a few more days to discuss some changes with certain designers and to decide which design will win.

Target Market(s)

(Insurance) Companies, partly also private clients.

Industry/Entity Type

Painting

Colors

Designer to choose colors to be used in the design.

Requirements
Must have
• All information (text, phone numbers, ...) of the old design ("old_letterhead_design.pdf") has also to be in the new one. Additional to that there are a few changes:
The phone numbers "01 583 61 47" and "01 583 61 37" change to "044 583 61 47" and "044 583 61 37". And please mention also this email address: gutachten@valmorkeller.example .

- The design should only be in the header-area of the A4-paper. An the background color of the A4-paper will be white.

- The design should consist of two designs. One for the first page and a smaller version of the design for the following pages.

- THE NEW DESIGN DOESN'T NEED A LOGO! You can make a design with geometric forms, ...

- The new design should have a juridical look. It should only contain colors like brown, fawn, black, light green, ...... colors which look serious/reliable.
Nice to have
• Geometric Forms, Symbols or other design elements.

- It would also be nice to have some design elements which emphasize the kind of work we are offering.

```html
<!DOCTYPE html>
<html lang="de">
<head>
<meta charset="utf-8">
<title>Briefpapier Valmor Keller</title>
<link rel="stylesheet" href="https://fonts.googleapis.com/css2?family=Source+Sans+3:wght@400;700&display=swap">
<style>
  :root {
    --backdrop: #ebebeb;
    --paper: #f8f8f8;
    --band: #3176ad;
    --band-text: #ffffff;
    --accent: #2c6aa3;
    --muted: #9a9a9a;
  }
  html, body {
    margin: 0;
    padding: 0;
    width: 1200px;
    height: 800px;
    overflow: hidden;
    background: var(--backdrop);
    font-family: "Source Sans 3", "Myriad Pro", Arial, sans-serif;
  }
  .sheet {
    position: absolute;
    width: 407px;
    height: 574px;
    background: var(--paper);
  }
  .sheet--first { left: 165px; top: 111px; }
  .sheet--following { left: 613px; top: 110px; }

  .service-band {
    height: 12px;
    background: var(--band);
    color: var(--band-text);
    font-size: 5px;
    display: flex;
    justify-content: center;
    align-items: center;
    gap: 5px;
    letter-spacing: 0.05px;
  }
  .service-band .divider { padding: 0 3px; }

  .sender {
    position: absolute;
    left: 9px;
    top: 19px;
    font-size: 7px;
    line-height: 10.5px;
    color: var(--muted);
  }
  .sender .sender-name {
    color: var(--accent);
    font-weight: 700;
  }
  .contact {
    position: absolute;
    right: 9px;
    top: 19px;
    text-align: right;
    font-size: 7px;
    line-height: 10.3px;
    color: var(--muted);
  }
  .contact .label {
    color: var(--accent);
    font-weight: 700;
  }
</style>
</head>
<body>
  <section class="sheet sheet--first" aria-label="Briefbogen erste Seite">
    <nav class="service-band">
      <span>Gutachten</span><span class="divider">|</span>
      <span>Expertisen</span><span class="divider">|</span>
      <span>Devisierungen</span><span class="divider">|</span>
      <span>Farbberatungen</span><span class="divider">|</span>
      <span>Dekorative Gestaltungen</span>
    </nav>
    <address class="sender" style="font-style:normal">
      <div class="sender-name">Valmor Keller</div>
      <div>eidg. dipl. Malermeister</div>
      <div>Lindenweg 7</div>
      <div>8805 Richterswil</div>
    </address>
    <address class="contact" style="font-style:normal">
      <div><span class="label">Telefon</span> 044 583 61 47</div>
      <div><span class="label">Fax</span> 044 583 61 37</div>
      <div><span class="label">Natel</span> 079 412 56 90</div>
      <div><span class="label">Email</span> gutachten@valmorkeller.example</div>
    </address>
  </section>

  <section class="sheet sheet--following" aria-label="Briefbogen Folgeseite">
    <nav class="service-band">
      <span>Gutachten</span><span class="divider">|</span>
      <span>Expertisen</span><span class="divider">|</span>
      <span>Devisierungen</span><span class="divider">|</span>
      <span>Farbberatungen</span><span class="divider">|</span>
      <span>Dekorative Gestaltungen</span>
    </nav>
  </section>
</body>
</html>
```